Refresh and update our Juice bottle label to a more vibrant and eye catching brand

We’ve had this label and included trademarked logo for the past 10 years. We do change the name of the juice ands its ingredients accordingly.
I want to up-date this round juice bottle label so it is more eye catching , trendy and clearly screams (healthy/juice/delicious/refreshing/beauty/youthful/high energy.
I have attached my trademarked logos as well as examples of a few labels. I also attached a few pictures of our juices with the current label which is a 2x4 inch front and back. I want you to see how colorful our juice is. I want the updated label to include out trademarked logo somehow but add in some color or graphics that speak to the message above in (). Open to adding color and even having a wrap around label instead of front and back=

Target Market(s)

Upscale women:men, age 20-65 40:30 ratio, health/ fitness/ body aware, anti aging/ high energy/ prevention of disease. Clientele is primarily caucasian.

Industry/Entity Type

Beverage, cold-pressed juice, wellness

Font styles to use
Sans Serif

Colors
59FF00
82FF00
B8FF75
E3FFCB
F4FFEA
EB3D1F
EC4F4E
F09395
F8D3D4
FCEDEE
E54698
E96AAD
F1A4CE
F9D9EA
FCEFF6
6B429C
8869AF
B7A5CE
E3DAEB
F3F0F8

Requirements
Must have
• My trademarked logo incorporated somehow. Bright/simple/modern/trendy style. I need to be able to change out the name of the juice and its ingredients and nutritional information. I want the label to say “100% Juice” basically this all needs to be on it: Name and Address. The name and address of your juicing business. ... Name of the Food. You should list the name of the food that is commonly used. ... What is the Amount of Juice inside of the bottle? ... % of juice declaration. ... Ingredients. ... Food Allergen (made in a facility with nuts). ... The Disclaimer. Must say “cold-pressed juice”
Nice to have
• Maybe a graphic image of a piece of fruit like a lemon with sliced cucumbers, I want vibrant colors added such as maybe use hot pink -outline or graphic on my Feel Rosy Bright? since the juice is pink. Or a bright yellow on my Zest Rising? Or a bright green on Lush Ace. Maybe some wording like “no added sugar or preservatives”, “gluten free”
Should not have
• No health guarantees

```html
<!DOCTYPE html>
<html lang="en">
<head>
<meta charset="utf-8">
<title>Verdant Sip – Cold-Pressed Juice Label</title>
<link href="https://fonts.googleapis.com/css2?family=Roboto:wght@300;400;500;700&family=Roboto+Slab:wght@700;800&family=Titan+One&display=swap" rel="stylesheet">
<style>
  :root{
    --bg:#808080;
    --paper:#ffffff;
    --paper-shade:#ececec;
    --green-dark:#1e6f27;
    --green:#3b8d1e;
    --lime:#8fb80a;
    --lime-bright:#7dbb16;
    --orange:#f5a41e;
    --yellow:#f9be1a;
    --ink:#3d3d3d;
    --ink-soft:#5a5a5a;
    --warn:#e5251b;
  }
  *{box-sizing:border-box;margin:0;padding:0}
  html,body{width:1200px;height:1013px;overflow:hidden}
  body{background:var(--bg);font-family:"Roboto",sans-serif;color:var(--ink);position:relative}

  .label{
    position:absolute;left:20px;top:216px;width:1160px;height:580px;
    background:linear-gradient(135deg,var(--paper-shade) 0%,var(--paper) 45%,var(--paper-shade) 100%);
    overflow:hidden;box-shadow:4px 6px 10px rgba(0,0,0,.25);
  }
  .label-waves{position:absolute;inset:0;width:100%;height:100%}

  .brand{position:absolute;display:flex;align-items:center;gap:8px;color:var(--green);font-weight:700}
  .brand-dot{border-radius:50%;background:var(--lime)}
  .brand--front{left:240px;top:48px;font-size:26px}
  .brand--front .brand-dot{width:26px;height:26px}
  .brand--back{left:616px;top:346px;font-size:17px}
  .brand--back .brand-dot{width:18px;height:18px}

  .front-copy{position:absolute;left:88px;width:400px;text-align:center}
  .kicker{top:120px;font-family:"Roboto Slab",serif;font-weight:800;font-size:28px;color:var(--green-dark)}
  .product-name{
    top:150px;font-family:"Titan One",sans-serif;font-size:112px;line-height:1;letter-spacing:2px;
    color:var(--yellow);-webkit-text-stroke:5px var(--green-dark);paint-order:stroke fill;
    text-shadow:5px 5px 0 var(--green-dark);
  }
  .juice-pill{
    position:absolute;left:210px;top:263px;width:157px;height:31px;border-radius:9px;
    background:var(--lime-bright);color:#fff;font-weight:300;font-size:21px;
    display:flex;align-items:center;justify-content:center;
  }
  .tagline{top:306px;font-weight:700;font-size:12.5px;color:var(--ink-soft);left:38px;width:500px}
  .fruit-art{
    position:absolute;left:72px;top:330px;width:460px;height:205px;border-radius:48% 52% 40% 45%;
    background:radial-gradient(ellipse at 35% 45%,#ffe04a 0%,#f7c81c 35%,#8cc43a 65%,#3f9b2a 100%);
    opacity:.92;
  }
  .net-wt{position:absolute;left:88px;width:400px;top:542px;text-align:center;color:#fff;font-weight:500;font-size:15px;letter-spacing:.3px}

  .panel{position:absolute;top:52px;height:190px;border:1.5px solid var(--green);border-radius:10px;background:rgba(255,255,255,.6)}
  .nutrition{left:613px;width:283px;font-size:8.5px;color:var(--ink-soft)}
  .nutrition-title{position:absolute;left:8px;top:4px;font-weight:700;font-size:22px;line-height:21px;color:var(--green-dark)}
  .nutrition-serving{position:absolute;left:8px;top:52px;width:95px;border-top:1px solid var(--green-dark);padding-top:3px;line-height:13px;font-size:9px}
  .nutrition-amount{position:absolute;left:8px;top:106px;width:95px;border-top:1px solid var(--green-dark);padding-top:2px;color:var(--lime-bright);font-weight:700;font-size:8px}
  .nutrition-calories{position:absolute;left:8px;top:120px;width:95px;border-top:1px solid var(--green-dark);padding-top:2px;color:var(--lime-bright);font-weight:700;font-size:14px}
  .nutrition-calories b{font-size:19px;font-weight:500}
  .nutrition-divider{position:absolute;left:104px;top:4px;height:146px;border-left:1px solid var(--green-dark)}
  .nutrition-divider--right{left:220px}
  .nutrient-list{position:absolute;left:108px;top:16px;width:175px;list-style:none;line-height:12.6px}
  .nutrient-list li{display:flex;justify-content:space-between;padding-right:14px}
  .nutrient-list .key{color:var(--lime-bright);font-weight:700}
  .nutrient-list .sub{padding-left:18px}
  .dv-head{position:absolute;right:8px;top:8px;font-size:7px;font-weight:700;color:var(--green-dark)}
  .nutrition-rule{position:absolute;left:8px;right:8px;top:150px;border-top:3px solid var(--green-dark)}
  .nutrition-note{position:absolute;left:14px;right:10px;top:157px;font-size:8.5px;line-height:11px}

  .ingredients{left:915px;width:202px;text-align:center;color:var(--ink-soft)}
  .ingredients h2{font-size:16px;font-weight:700;color:var(--green-dark);margin-top:5px;padding-bottom:5px;border-bottom:1px solid var(--green);margin-left:12px;margin-right:12px}
  .ingredient-list{font-size:8.8px;line-height:12px;margin-top:9px}
  .best-by{font-size:12.5px;font-weight:700;color:var(--green);line-height:16px;margin-top:14px}
  .storage{font-size:8.3px;line-height:14.5px;margin-top:5px}
  .natural-tag{display:inline-block;background:var(--lime-bright);color:#fff;font-size:8px;border-radius:3px;padding:0 6px;line-height:10px}

  .warning{position:absolute;left:616px;top:268px;width:280px;font-size:12px;line-height:14.8px;font-weight:300;color:var(--ink)}
  .warning strong{color:var(--warn);font-weight:400}
  .eco-icons{position:absolute;left:953px;top:271px;display:flex;gap:12px}
  .eco-icons svg{width:37px;height:37px}

  .address{position:absolute;left:616px;top:398px;font-size:12px;line-height:15px;color:var(--ink)}
  .web{position:absolute;left:616px;top:432px;font-size:16px;color:var(--green);letter-spacing:.3px}
  .batch{position:absolute;left:937px;top:376px;font-size:9.5px;line-height:17.5px;color:var(--ink-soft)}
</style>
</head>
<body>
<section class="label">
  <svg class="label-waves" viewBox="0 0 1160 580" preserveAspectRatio="none" aria-hidden="true">
    <path d="M0 415 C250 350 420 400 560 470 C720 545 900 520 1160 440 L1160 580 L0 580 Z" fill="#f5a41e"/>
    <path d="M0 428 C250 365 420 415 560 482 C720 555 900 530 1160 452 L1160 580 L0 580 Z" fill="#ffffff"/>
    <defs>
      <linearGradient id="bandGreen" x1="0" x2="1" y1="0" y2="0">
        <stop offset="0" stop-color="#1f7a2a"/>
        <stop offset="0.55" stop-color="#3e8e1f"/>
        <stop offset="1" stop-color="#8fb80a"/>
      </linearGradient>
    </defs>
    <path d="M0 440 C250 380 420 430 560 495 C720 565 900 545 1160 466 L1160 580 L0 580 Z" fill="url(#bandGreen)"/>
  </svg>

  <div class="brand brand--front"><span class="brand-dot"></span>Verdant Sip</div>
  <div class="front-copy kicker">Cold-Pressed</div>
  <div class="front-copy product-name">JUICE</div>
  <div class="juice-pill">100% Juice</div>
  <div class="front-copy tagline">Healthy, Juice, Delicious, Refreshing, Beauty, Youthful, High Energy</div>
  <div class="fruit-art" role="img" aria-label="Illustration of lemon slices, a whole lemon half with leaves and sliced cucumbers"></div>
  <div class="net-wt">Net Wt. 12oz (354mL)</div>

  <div class="panel nutrition">
    <div class="nutrition-title">Nutrition<br>Facts</div>
    <div class="nutrition-serving">Serving size<br>1/4 cup (38g)<br>8 Serving per<br>container</div>
    <div class="nutrition-amount">Amount Per Serving</div>
    <div class="nutrition-calories">Calories <b>190</b></div>
    <div class="nutrition-divider"></div>
    <div class="nutrition-divider nutrition-divider--right"></div>
    <div class="dv-head">% Daily Value*</div>
    <ul class="nutrient-list">
      <li class="key">Total Fat 15g</li>
      <li class="sub"><span>Saturated Fat</span><span>21%</span></li>
      <li class="sub"><span>Trans Fat</span><span>21%</span></li>
      <li class="sub"><span>Polyunsaturated Fat</span><span>21%</span></li>
      <li class="sub"><span>Monounsaturated Fat</span><span>21%</span></li>
      <li><span class="key">Cholesterol 10mg</span><span>1%</span></li>
      <li><span class="key">Sodium 10mg</span><span>1%</span></li>
      <li><span class="key">Total Carbohydrate 10g</span><span>1%</span></li>
      <li class="sub"><span>Sugar</span><span></span></li>
      <li><span class="key">Protein 5g</span><span>0%</span></li>
    </ul>
    <div class="nutrition-rule"></div>
    <p class="nutrition-note">* Percent Daily Values are based on a 2,000 calorie diet. Your daily values may be higher or lower depending on your calorie needs.</p>
  </div>

  <div class="panel ingredients">
    <h2>Ingredients</h2>
    <p class="ingredient-list">Beets + Stems • Spinach • Cucumber<br>Green Apple • Parsley • Lemon</p>
    <p class="best-by">Best if Used Within 5 days of Purchase</p>
    <p class="storage">100% VEGETABLE &amp; FRUIT JUICE<br>Perishable Keep Refrigerated<br>Shake Well<br><span class="natural-tag">*separation is natural*</span></p>
  </div>

  <p class="warning"><strong>WARNING:</strong> This product has not been pasteurized and, therefore may contain harmful bacteria that can cause serious illness in children, the elderly, and persons with weakened immune systems.</p>

  <div class="eco-icons">
    <svg viewBox="0 0 40 40" role="img" aria-label="Recyclable">
      <circle cx="20" cy="20" r="18" fill="none" stroke="#222" stroke-width="2.5"/>
      <path d="M14 15 L19 10 L23 15 M27 19 L28 26 L21 27 M13 24 L14 28 L21 28" fill="none" stroke="#222" stroke-width="2.2" stroke-linejoin="round"/>
    </svg>
    <svg viewBox="0 0 40 40" role="img" aria-label="Dispose in bin">
      <circle cx="20" cy="20" r="18" fill="none" stroke="#222" stroke-width="2.5"/>
      <circle cx="15" cy="13" r="2.2" fill="#222"/>
      <path d="M19 15 h9 M20 15 l1 14 h5 l1 -14 M13 17 l2 7 -2 6" fill="none" stroke="#222" stroke-width="2"/>
    </svg>
  </div>

  <div class="brand brand--back"><span class="brand-dot"></span>Verdant Sip</div>
  <p class="address">4180 Orchard Bend #9, Meadowvale<br>CA 90000</p>
  <p class="web">verdantsip.com</p>
  <p class="batch">BATCH NO.<br>MFG.DATE<br>M.R.P.<br>(Inclusive of all taxes)</p>
</section>
</body>
</html>
```